Simple elegant business card

General card for a fin and television director.
Just want name, email, phone and address.

Target Market(s)

Prospective employers

Industry/Entity Type

Business

Requirements
Must have
• As above
Nice to have
• Logo but not necessary.
Should not have
• Not too colourful or funky.
• Simplicity and elegance the way to go.

```html
<!DOCTYPE html>
<html lang="en">
<head>
<meta charset="utf-8">
<title>Lena Marsh – Business Card</title>
<link rel="stylesheet" href="https://fonts.googleapis.com/css2?family=Poppins:wght@200;300&display=swap">
<style>
  :root {
    --page-bg: #d9d9db;
    --card-front: #fbfbfb;
    --card-back: #0f1420;
    --ink: #2a2a2a;
    --ink-back: #3b4150;
    --shadow: rgba(0, 0, 0, 0.18);
  }
  * { margin: 0; padding: 0; box-sizing: border-box; }
  html, body {
    width: 1200px;
    height: 900px;
    overflow: hidden;
    background: var(--page-bg);
  }
  .canvas {
    width: 1200px;
    height: 900px;
    display: flex;
    flex-direction: column;
    align-items: center;
    justify-content: center;
    gap: 56px;
  }
  .card {
    width: 640px;
    height: 366px;
    position: relative;
    box-shadow: 0 10px 30px var(--shadow);
    font-family: "Poppins", sans-serif;
  }
  .card--back {
    background: var(--card-back);
    display: flex;
    align-items: center;
    justify-content: center;
  }
  .card--front {
    background: var(--card-front);
  }
  .wordmark {
    font-weight: 200;
    font-size: 64px;
    letter-spacing: -1px;
    line-height: 1;
    text-transform: lowercase;
  }
  .card--back .wordmark {
    color: var(--ink-back);
    font-size: 72px;
  }
  .card--front .wordmark {
    color: var(--ink);
    position: absolute;
    top: 62px;
    left: 0;
    right: 0;
    text-align: center;
  }
  .contact {
    position: absolute;
    top: 198px;
    left: 0;
    right: 0;
    text-align: center;
    color: var(--ink);
    font-weight: 300;
    font-style: normal;
  }
  .contact__name {
    font-size: 19px;
    margin-bottom: 6px;
  }
  .contact__line {
    font-size: 15px;
    line-height: 1.6;
  }
</style>
</head>
<body>
  <main class="canvas">
    <section class="card card--back" aria-label="Card back">
      <div class="wordmark">lena marsh</div>
    </section>
    <section class="card card--front" aria-label="Card front">
      <div class="wordmark">lena marsh</div>
      <address class="contact">
        <div class="contact__name">Lena Marsh</div>
        <div class="contact__line">lenamarsh@mailbox.com</div>
        <div class="contact__line">+1 310 555 0142</div>
      </address>
    </section>
  </main>
</body>
</html>
```